Education Website Re-Design for Non-Profit

We are looking for a re-design of our education website, the KVR Learning center. The Learning Center is intended to be the "go to" resource for interactive classrooms and resources on chronic kidney disease and dialysis for patients, family members and interested parties. We are looking for a re-design on the home page and then design the basic pages that host the content on the site. Also, the classroom pages could use a revamp with a Left-Right Menus (nav on left vs. right)

Current website: www.kvrlearnhub.org
Example Basic Page: http://kvrlearnhub.org/diabetes-awareness-month
Classroom Page: http://kvrlearnhub.org/classroom/home-hemodialysis
Updates

Project Deadline Extended
Reason: Need more time to decide on current submissions.

Target Market(s)

Current patients, family members, healthcare professionals

Industry/Entity Type

Education

Coding

Coded - Design and coding required

Number of Pages Required

3 page

Font styles to use
Sans Serif

Colors
0355a3
3176b5
ec1f27
ffffff

Requirements
Must have
• The website is hosted using Drupal 7 and will likely be upgraded to Drupal 8 so as much compatibility with Drupal as possible would be nice. Also we would like it to be a responsive design with two breakpoints for phone/tablet and then tablet/desktop views. Please keep the branding colors and fonts the same as found in the attached draft style guide.
• I'm attaching a screen shot of the Northfield Wellness Alliance website. We like the layout and cleanliness of the information presented on their homepage and then their subsequent education pages. (url:http://www.wellnorthalliance.org/?loc=bb)
Nice to have
• I would like to see a clean, semi-modern design. I currently HATE the narrow fixed width design we have with the puzzle piece navigation objects
• Education Topics: Nutrition, Pediatric Kidney Disease, Diabetes, Bone and Mineral Disease, Treatment Options, Heart Disease, Mental Health, Chronic Kidney Disease, CKD Prevention, Emergency Preparedness, Anemia Management and Paying for Dialysis (Like bottom of Northfield Wellness Alliance)
Should not have
• Narrow fixed width design, white background around text makes it look disjointed and dated, no "educational tools" menu/subpage focus, shouldn't prioritize "advocacy" portion, it should be included but at the bottom. Education topics and tools need to be prioritized.

```html
<!DOCTYPE html>
<html lang="en">
<head>
<meta charset="utf-8">
<title>KVR Learning Center – Home</title>
<link href="https://fonts.googleapis.com/css2?family=Open+Sans:ital,wght@0,300;0,400;0,600;0,700;1,400&display=swap" rel="stylesheet">
<style>
:root{
  --navy:#1d3f73;
  --blue:#0355a3;
  --sky:#2ba6e0;
  --green:#6cbd45;
  --ink:#333a40;
  --muted:#6b7177;
  --dark:#23282d;
  --line:#d7dadd;
  --white:#ffffff;
}
*{margin:0;padding:0;box-sizing:border-box}
html,body{width:1200px;height:2765px;overflow:hidden}
body{font-family:"Open Sans",Arial,sans-serif;color:var(--ink);background:var(--white);position:relative}
section,header,footer{position:absolute;left:0;width:1200px}
.photo{position:absolute}
.btn{position:absolute;display:flex;align-items:center;justify-content:center;color:var(--white);font-size:16px}

/* header */
.site-header{top:0;height:55px;background:var(--white);z-index:3;box-shadow:0 1px 3px rgba(0,0,0,.1)}
.brand{position:absolute;left:115px;top:6px;display:flex;align-items:center;gap:8px}
.brand-mark{width:40px;height:40px;background:var(--blue)}
.brand-name{font-weight:700;font-size:15px;line-height:16px;color:var(--blue);text-transform:uppercase}
.main-nav{position:absolute;left:459px;top:19px;display:flex;gap:26px;font-size:11px;font-weight:600;color:var(--muted);text-transform:uppercase;align-items:center}
.main-nav .active{color:var(--ink)}
.main-nav .join{background:var(--sky);color:var(--white);padding:3px 9px}
.header-social{position:absolute;left:1058px;top:0;width:30px;height:55px;border-left:1px solid var(--line);display:flex;flex-direction:column;align-items:center;justify-content:center;gap:14px}
.header-social span{width:10px;height:10px;background:var(--ink);border-radius:50%}

/* hero */
.hero{top:0;height:575px}
.hero .photo{inset:0;background:linear-gradient(90deg,#cfc8be 0%,#b9a98f 45%,#d9cdbd 70%,#efe9e1 100%)}
.hero-panel{position:absolute;left:127px;top:182px;width:487px;height:266px;background:rgba(12,72,130,.88);color:var(--white);padding:26px 18px}
.hero-panel h1{font-weight:400;font-size:39px;line-height:44px}
.hero-panel p{font-size:13px;line-height:19px;margin-top:20px}
.hero .more{left:127px;top:462px;width:243px;height:36px;background:var(--dark)}
.hero .join-btn{left:376px;top:462px;width:238px;height:36px;background:var(--sky)}

/* featured */
.featured{top:575px;height:373px}
.section-title{position:absolute;left:140px;font-weight:300;font-size:40px;color:var(--ink)}
.section-rule{position:absolute;left:140px;width:916px;height:1px;background:var(--line)}
.green-btn{background:var(--green);width:199px;height:36px;font-size:15px}
.featured .section-title{top:55px}
.featured .section-rule{top:108px}
.featured .green-btn{left:857px;top:69px}
.body-text{position:absolute;left:150px;width:910px;font-size:15px;line-height:24px;color:#444}
.featured .body-text{top:133px}
.arrow{position:absolute;top:194px;width:39px;height:39px;background:#9cd2ee}
.arrow svg{width:39px;height:39px;display:block}
.arrow.prev{left:83px}.arrow.next{left:1078px}
.news-label{position:absolute;left:150px;top:230px;font-size:14px;color:#444}
.news-link{position:absolute;left:150px;top:257px;font-size:14px;color:var(--blue)}
.news-date{position:absolute;right:130px;top:232px;font-size:15px;color:#444}

/* ebola */
.alert-band{top:948px;height:435px}
.alert-band .photo{inset:0;background:linear-gradient(90deg,#a8867a 0%,#d9b7a6 30%,#e6dcd6 55%,#c7c1bf 100%)}
.alert-panel{position:absolute;left:583px;top:94px;width:590px;height:258px;background:rgba(43,166,224,.88);color:var(--white);padding:26px 24px}
.alert-panel h2{font-weight:400;font-size:34px;line-height:38px;width:440px}
.alert-panel p{font-size:14px;line-height:20px;margin-top:12px}

/* education */
.education{top:1383px;height:345px}
.education .section-title{top:42px}
.education .section-rule{top:94px}
.education .green-btn{left:857px;top:51px}
.education .p1{top:118px}
.education .p2{top:214px}

/* testimonials */
.testimonials{top:1728px;height:434px}
.testimonials .photo{inset:0;background:linear-gradient(90deg,#7f8a6b 0%,#9aa58a 35%,#c7b7a0 55%,#3e4a42 100%)}
.quote-panel{position:absolute;left:105px;top:78px;width:525px;height:254px;background:rgba(108,189,69,.9);color:var(--white);padding:30px 36px 24px 66px}
.quote-panel h2{font-weight:400;font-size:38px;line-height:50px}
.quote-panel p{font-size:16px;line-height:23px;font-style:italic;margin-top:10px;opacity:.9}
.quote-panel .author{font-style:normal;font-size:13px;margin-top:12px}
.qmark{position:absolute;font-size:80px;font-weight:700;line-height:1;color:var(--white)}
.qmark.open{left:8px;top:-10px}.qmark.close{right:12px;bottom:-40px}

/* contact */
.contact{top:2162px;height:438px;background:var(--white);overflow:hidden}
.contact .decor{position:absolute;inset:0}
.contact .kicker{position:absolute;left:0;width:1200px;top:52px;text-align:center;font-size:15px}
.contact h2{position:absolute;left:0;width:1200px;top:70px;text-align:center;font-weight:300;font-size:52px;color:var(--ink)}
.newsletter{position:absolute;left:152px;top:147px;width:415px;height:39px;border:2px solid var(--green);display:flex;background:var(--white)}
.newsletter span{flex:1;font-size:14px;padding:8px 10px;color:#555}
.newsletter b{width:44px;background:var(--green);color:var(--white);font-weight:400;display:flex;align-items:center;justify-content:center}
.contact .donate{left:583px;top:147px;width:462px;height:39px;background:var(--sky);font-size:18px}
.footer-brand{position:absolute;left:110px;top:240px;display:flex;flex-direction:column;align-items:flex-start;gap:8px}
.footer-brand .brand-mark{width:100px;height:100px;background:var(--navy)}
.footer-brand .brand-name{font-size:14px;color:var(--navy);width:180px}
.footer-col{position:absolute;top:240px;font-size:13px;line-height:28px;color:#444}
.footer-col h3{font-weight:400;font-size:21px;color:var(--ink);border-bottom:1px solid var(--line);width:130px;margin-bottom:8px;line-height:32px}
.footer-col .lbl{color:var(--green)}
.footer-col li{list-style:none;display:flex;gap:8px;align-items:flex-start}
.footer-col svg{flex:none;margin-top:8px}

/* bottom bar */
.bottom-bar{top:2600px;height:165px;background:var(--dark)}
.social{position:absolute;left:0;width:1200px;top:66px;display:flex;justify-content:center;gap:16px}
.social span{width:16px;height:16px;border-radius:50%;background:var(--white)}
.copyright{position:absolute;left:0;width:1200px;top:100px;text-align:center;font-size:12px;color:#cfd3d6}
</style>
</head>
<body>

<header class="site-header">
  <div class="brand"><span class="brand-mark"></span><span class="brand-name">KVR<br>Learning Center</span></div>
  <nav class="main-nav">
    <span class="active">Home</span><span>Fundraise</span><span>Donate</span><span>Patient &amp; Family Resources</span><span>Policy</span><span>Donate</span><span class="join">Join Us</span>
  </nav>
  <div class="header-social"><span></span><span></span></div>
</header>

<section class="hero">
  <div class="photo" role="img" aria-label="Smiling young woman holding books in a library"></div>
  <div class="hero-panel">
    <h1>Improving Our Lives<br>Through Empowerment</h1>
    <p>The Center is dedicated to improving kidney patients' quality of life and reducing the occurrence of ESRD through education and by developing awareness of dialysis and kidney disease issues, improving the partnership between patients and caregivers, and developing favorable public policy solutions.</p>
  </div>
  <div class="btn more">More About KVR</div>
  <div class="btn join-btn">Join Our Community</div>
</section>

<section class="featured">
  <h2 class="section-title">Diabetes Awareness Month:</h2>
  <div class="section-rule"></div>
  <div class="btn green-btn">View All Places</div>
  <div class="arrow prev"><svg viewBox="0 0 39 39"><path d="M23 12l-8 7.5 8 7.5" fill="none" stroke="#fff" stroke-width="3"/></svg></div>
  <div class="arrow next"><svg viewBox="0 0 39 39"><path d="M16 12l8 7.5-8 7.5" fill="none" stroke="#fff" stroke-width="3"/></svg></div>
  <p class="body-text">Diabetes is the most common cause of kidney disease, accounting for nearly 44% of new cases each year. Coinciding with Diabetes Awareness Month, we were pleased to host an education call on November 3 to discuss the physiology of diabetes in Chronic Kidney Disease patients as well as beneficial lifestyle interventions. Danielle</p>
  <div class="news-label">KVR News</div>
  <div class="news-link">Honoring My Father on PKD Awareness Day</div>
  <div class="news-date">Wed, 09/03/2014 - 8:00pm</div>
</section>

<section class="alert-band">
  <div class="photo" role="img" aria-label="Group of smiling students gathered around a laptop"></div>
  <div class="alert-panel">
    <h2>Proper Disinfection Practices Can Eliminate The Spread of Ebola</h2>
    <p>Dialysis facilities have infection control policies and procedures in place to protect their patients and staff from coming in contact with any blood borne diseases, but diligence in following those policies and procedures is imperative to protect us all.</p>
  </div>
</section>

<section class="education">
  <h2 class="section-title">Education :</h2>
  <div class="section-rule"></div>
  <div class="btn green-btn">Join us</div>
  <p class="body-text p1">Learn about issues affecting people with kidney disease.Education is KEY and an important tool in the fight against kidney disease. Whether you have just been diagnosed with Chronic Kidney Disease (CKD) or you have been on dialysis for years, let us help you better understand the disease, dialysis, and the steps you can take in combating it.</p>
  <p class="body-text p2">Like diabetes and high blood pressure, Chronic Kidney Disease (CKD) is called a "silent killer" because there are few symptoms and by the time a person realizes they have a problem, damage has been done. Learn about CKD, who is affected, and what can be done to prevent it.</p>
</section>

<section class="testimonials">
  <div class="photo" role="img" aria-label="Students laughing together around a laptop outdoors"></div>
  <div class="quote-panel">
    <span class="qmark open">&ldquo;</span>
    <h2>Testimonials</h2>
    <p>@CareVoices has released a statement expressing concerns with the #CARE 5-star program. See it here: http://lnk.to/kv7Q2</p>
    <p class="author">Martin Avery</p>
    <span class="qmark close">&rdquo;</span>
  </div>
</section>

<section class="contact">
  <svg class="decor" viewBox="0 0 1200 438" aria-hidden="true">
    <g stroke="#e4e6e8" stroke-width="14" fill="none">
      <path d="M-40 230L260 -20"/><path d="M-40 300L330 -10"/><path d="M-40 160L180 -20"/>
      <path d="M1240 60L960 438"/><path d="M1240 160L1030 438"/><path d="M1240 -10L900 438"/>
    </g>
  </svg>
  <p class="kicker">How can we help you?</p>
  <h2>LET'S TALK</h2>
  <div class="newsletter"><span>Email Newsletters</span><b>Go</b></div>
  <div class="btn donate">Donate Now</div>

  <div class="footer-brand"><span class="brand-mark"></span><span class="brand-name">KVR Learning Center</span></div>

  <div class="footer-col" style="left:321px"><h3>Links</h3>
    <ul><li>About</li><li>Values</li><li>Board Members</li><li>Financials</li><li>Staff</li></ul></div>
  <div class="footer-col" style="left:489px"><h3>About KVR</h3>
    <ul><li>Our Work</li><li>Mission</li><li>Chronic Diseases</li><li>Patient Resources</li><li>Donate</li></ul></div>
  <div class="footer-col" style="left:666px"><h3>KVR</h3>
    <ul><li>Education</li><li>Advocacy</li><li>Join Us</li><li>Contact Us</li><li>FAQS</li></ul></div>
  <div class="footer-col" style="left:830px"><h3>Contact Us</h3>
    <ul>
      <li><svg width="12" height="12" viewBox="0 0 12 12"><path d="M2 1l2 0 1 3-1.5 1a7 7 0 0 0 3.5 3.5L8 7l3 1 0 2c0 1-1 1.5-2 1.5A9 9 0 0 1 .5 3C.5 2 1 1 2 1z" fill="#3a7d2a"/></svg><span><span class="lbl">Toll-free :</span> 1-800-555-0142</span></li>
      <li><svg width="12" height="10" viewBox="0 0 12 10"><rect x=".5" y=".5" width="11" height="9" fill="#3a7d2a"/><path d="M.5 .5l5.5 5 5.5-5" stroke="#fff" fill="none"/></svg><span><span class="lbl">Email :</span> info@kvrlearnhub.org</span></li>
      <li><svg width="10" height="14" viewBox="0 0 10 14"><path d="M5 0a5 5 0 0 1 5 5c0 4-5 9-5 9S0 9 0 5a5 5 0 0 1 5-5z" fill="#3a7d2a"/><circle cx="5" cy="5" r="2" fill="#fff"/></svg><span style="line-height:20px;margin-top:4px"><span class="lbl">Adress :</span> 240 Harbor Lane, Suite 310<br>Northfield, ST 00000</span></li>
    </ul></div>
</section>

<footer class="bottom-bar">
  <div class="social" aria-label="Social links"><span></span><span></span><span></span><span></span></div>
  <p class="copyright">© Copyright all right reserved &nbsp;2015 @kvrlearnhub.org</p>
</footer>

</body>
</html>
```